Modern and appealing business Wordpress site

I've been operating my consulting firm for 5 years and feel like it is time to really improve on my web presence as I'm starting to get more national attention. I had a logo made through this service a couple of years ago, and would like to get a website that matches the look of it. The website will be used to (1) advertise my services (2) provide a brief overview of our management philosophies, and (3) host a resource library database. I understand HTML, but am not as familiar with how to code Wordpress, so I need someone that can help upload themes.

The website can be found at www.trbvexlane.com.

For design, I prefer round designs to square and want the color scheme to match the attached logo. I have included both the full logo and the abbreviated one.

I also have a new picture for CFO uploaded. I plan on getting a new one for the CEO in the coming weeks, so I would like someone that I could get to help make the modification at a later time.

The resource database will be put into a document library (probably Plix4) once the final design is completed rather than having multiple pages with links...just so you know the final vision for the site.

Reach out if you have any questions.

Target Market(s)

Community Action Agencies, Nonprofit Organization Leaders

Industry/Entity Type

Consulting

Coding

Coded - Design and coding required

Font styles to use
Sans Serif

Requirements
Must have
• Must match the color scheme of the attached logo

```html
<!DOCTYPE html>
<html lang="en">
<head>
<meta charset="utf-8">
<title>Trbvex Lane, LLC</title>
<link href="https://fonts.googleapis.com/css2?family=Outfit:wght@300;400;500;600;700&display=swap" rel="stylesheet">
<style>
:root{
  --ink:#1f1f1f;
  --text:#3a3a3a;
  --brand:#2f9fd8;
  --brand-dark:#1f6fc0;
  --cyan:#00d0f5;
  --aqua:#1ef8f0;
  --sky:#45b9e2;
  --footer:#2fa5d9;
  --white:#ffffff;
}
*{box-sizing:border-box;margin:0;padding:0}
html,body{width:1200px;height:3552px;overflow:hidden}
body{position:relative;font-family:"Outfit",sans-serif;color:var(--text);background:var(--white)}
.abs{position:absolute}
.site-header{position:absolute;left:0;top:0;width:1200px;height:90px;z-index:5}
.logo{display:flex;align-items:center;gap:14px;font-weight:600;color:var(--brand);letter-spacing:1px}
.logo .mark{border-radius:50%;background:var(--brand)}
.nav{top:34px;left:571px;display:flex;gap:30px;font-size:11px;font-weight:500;color:var(--ink);letter-spacing:.3px}
.hero{top:0;left:0;width:1200px;height:501px;background:linear-gradient(180deg,#f2f3f2 0%,#e6e8e3 55%,#8a6a4a 78%,#4a3322 100%)}
.hero h1{position:absolute;left:283px;top:200px;font-size:36px;line-height:41px;font-weight:600;color:var(--ink)}
.photo{position:absolute}
.about-box{left:152px;top:589px;width:620px;height:308px;border:2px solid var(--ink);background:var(--white);padding:44px 82px 0 92px;font-size:18.5px;line-height:24.5px;font-weight:300;color:var(--ink)}
.about-box .name{font-size:29px;color:var(--brand);font-weight:400}
.mission-band{left:0;top:955px;width:1200px;height:297px;background:var(--cyan);border-bottom:3px solid var(--ink)}
.mission-card{left:330px;top:955px;width:259px;height:270px;background:var(--white);border-radius:0 0 8px 8px;padding:14px 22px 0 29px}
.mission-card h2{font-size:26px;line-height:28px;font-weight:600;color:var(--ink);margin-bottom:20px}
.mission-card p{font-size:14px;line-height:19.5px;font-weight:300;color:var(--ink)}
.label{background:var(--white);border:2px solid var(--ink);font-size:14px;line-height:22px;color:var(--ink);padding:0 14px;display:flex;flex-direction:column;justify-content:center;white-space:nowrap}
.band-aqua{background:var(--aqua)}
.band-sky{background:var(--sky)}
.icon-badge{width:76px;height:76px;border-radius:50%;background:var(--white);display:flex;align-items:center;justify-content:center;box-shadow:0 2px 8px rgba(0,0,0,.12)}
.service h3{font-size:25px;font-weight:400;margin-bottom:18px}
.service p{font-size:14.5px;line-height:18.7px;font-weight:300}
.service.light{color:var(--white)}
.service.dark{color:var(--ink)}
.quote{border:2px solid #555;border-radius:6px;background:var(--white);font-size:15px;line-height:20px;font-weight:500;color:var(--ink)}
.quote .by{display:block;margin-top:20px;font-size:10.5px;line-height:15px;color:var(--brand-dark);font-weight:500}
.quote .tail{position:absolute;bottom:-14px;width:24px;height:14px}
.qmark{font-size:56px;line-height:40px;font-weight:700;color:var(--ink);background:var(--white);padding:0 4px}
.footer{left:0;top:3338px;width:1200px;height:214px;background:var(--footer);color:var(--white)}
.footer .addr{position:absolute;left:334px;top:113px;font-size:11.5px;line-height:18px;font-weight:500;letter-spacing:1px}
.footer .btn{position:absolute;left:331px;top:172px;width:91px;height:28px;border-radius:4px;background:var(--brand-dark);font-size:9px;font-weight:600;letter-spacing:1px;display:flex;align-items:center;justify-content:center}
.footer .links{position:absolute;left:550px;top:50px;font-size:9.5px;line-height:18px;font-weight:500;letter-spacing:.6px;list-style:none}
.footer .copy{position:absolute;left:748px;top:71px;font-size:10.5px}
.footer .social{position:absolute;left:746px;top:94px;display:flex;gap:5px}
.footer .social span{width:28px;height:28px;border-radius:50%;border:2px solid var(--white);background:rgba(255,255,255,.15)}
</style>
</head>
<body>

<section class="abs hero" role="img" aria-label="Young plants sprouting from soil beside stacks of gold coins">
  <h1>Leading Organizations<br>to Excellence!</h1>
</section>

<header class="site-header">
  <div class="abs logo" style="left:232px;top:22px;font-size:28px">
    <span class="mark" style="width:48px;height:48px"></span>TRBVEX LANE
  </div>
  <nav class="abs nav"><span>HOME</span><span>SERVICES</span><span>ROMA</span><span>MADD</span><span>RESOURCES</span><span>CONTACT</span></nav>
</header>

<section class="about">
  <div class="photo" style="left:589px;top:501px;width:611px;height:454px;background:linear-gradient(135deg,#b9c9cf,#5f7780 60%,#33434a)" role="img" aria-label="Two businesswomen smiling while reviewing a tablet at an office table"></div>
  <div class="abs about-box"><span class="name">Trbvex Lane, LLC</span> was created to help nonprofits and government contractors meet their basic funding requirements and adopt a Mission Aligned Data Driven mindset that promotes positive change in the lives of the people they serve. Our approach is not simply based off of theoretical business practices, but on practical solutions to real-life situations learned through more than twenty years of experience.</div>
</section>

<section class="mission">
  <div class="abs mission-band"></div>
  <div class="abs" style="left:589px;top:1020px;width:611px;height:232px;background:linear-gradient(90deg,rgba(0,0,0,0),rgba(0,90,130,.12))" role="img" aria-label="Line drawing of growing money plants under a rising arrow"></div>
  <div class="abs mission-card">
    <h2>Our<br>Mission.</h2>
    <p>To help social service organizations develop a Mission Aligned Data Driven mindset that promotes positive change in the lives of the customers they serve.</p>
  </div>
</section>

<section class="team">
  <div class="photo" style="left:368px;top:1303px;width:284px;height:239px;background:linear-gradient(160deg,#8fa58a,#4d5a55 55%,#1f2733)" role="img" aria-label="Portrait of the CEO in a suit outdoors"></div>
  <div class="abs label" style="left:243px;top:1365px;width:175px;height:119px">Our CEO<br>Dorian “Reed” Vexlane</div>
  <div class="photo" style="left:677px;top:1303px;width:196px;height:242px;background:linear-gradient(160deg,#5e6e86,#8a7a68 55%,#4a5660)" role="img" aria-label="Portrait of the CFO against a blue backdrop"></div>
  <div class="abs label" style="left:774px;top:1444px;width:182px;height:128px">Our CFO<br>Marisol Keane Vexlane</div>
</section>

<section class="services">
  <div class="abs band-aqua" style="left:0;top:1601px;width:360px;height:1201px"></div>
  <div class="abs band-sky" style="left:360px;top:1601px;width:840px;height:1201px"></div>

  <div class="photo" style="left:88px;top:1652px;width:475px;height:315px;background:linear-gradient(135deg,#c8b8a4,#7d6a58 55%,#3b3a3f)" role="img" aria-label="Team meeting around a table with laptops"></div>
  <div class="abs icon-badge" style="left:54px;top:1758px">
    <svg width="36" height="36" viewBox="0 0 36 36" fill="none" stroke="#e0413a" stroke-width="2"><rect x="4" y="5" width="28" height="26" rx="2"/><circle cx="14" cy="15" r="4"/><path d="M8 27c1-5 11-5 12 0M22 12h6M22 17h6M22 22h4"/></svg>
  </div>
  <div class="abs service light" style="left:608px;top:1717px;width:340px">
    <h3>Training &amp; Consulting</h3>
    <p>We are dedicated to the success of our customers and offer a variety of services focused on improving organizational efficiency and effectiveness through implementation of the Mission Aligned Data Driven (MADD) mindset and the Results Oriented Management and Accountability (ROMA) system of organizational management.</p>
  </div>

  <div class="abs" style="left:0;top:1968px;width:712px;height:456px;background:var(--white)"></div>
  <div class="photo" style="left:713px;top:2022px;width:487px;height:347px;background:radial-gradient(circle at 50% 50%,#3a2a20,#0b1a24 60%,#0a2a3a)" role="img" aria-label="Abstract digital data streams in blue and orange light"></div>
  <div class="abs service dark" style="left:283px;top:2075px;width:335px">
    <h3>Data Analytics</h3>
    <p>One the most important, and frequently neglected, areas of organizational management is the analysis of data to accurately identify community needs and track progress towards the successful fulfillment of the entity’s purpose. Our goal is to ensure each of our customers is equipped with the tools necessary to obtain objective data that will allow for quality decision making.</p>
  </div>
  <div class="abs icon-badge" style="left:674px;top:2132px">
    <svg width="40" height="36" viewBox="0 0 40 36" fill="none" stroke="#f07a2a" stroke-width="2.4" stroke-linecap="round"><path d="M6 32V20M14 32V14M22 32V22M30 32V16M36 32V24M4 34h34"/><path d="M5 12l9-6 8 5 12-7"/></svg>
  </div>

  <div class="photo" style="left:92px;top:2450px;width:472px;height:287px;background:linear-gradient(135deg,#e9ece6,#b7b7ad 50%,#4a3a30)" role="img" aria-label="Presenter at a flip chart speaking to a seated group"></div>
  <div class="abs icon-badge" style="left:54px;top:2544px">
    <svg width="36" height="34" viewBox="0 0 36 34" fill="none" stroke="#3a4fb0" stroke-width="2"><rect x="4" y="12" width="28" height="19" rx="2"/><path d="M4 12l2-7 26 0-2 7M11 5l-2 7M19 5l-2 7M27 5l-2 7"/><path d="M15 17v9l8-4.5z" fill="#3a4fb0"/></svg>
  </div>
  <div class="abs service light" style="left:608px;top:2497px;width:345px">
    <h3>Storytelling</h3>
    <p>Trbvex Lane, LLC is dedicated to ensuring each of our customers is provided with the tools necessary to tell their story through the generation of graphic reports, outreach tools, and videos so they can increase community support and involvement, allowing for a reduced reliance on government funding.</p>
  </div>
</section>

<section class="testimonials">
  <div class="abs quote" style="left:324px;top:2880px;width:269px;height:310px;padding:44px 22px 0 25px">“It was a training, but not your typical training. It leaves you with a new and different take on things. You will find yourself saying ‘Wow, I’ve never thought of it like that before’. You will be left with new and refreshing ideas and different ways to approach situations.”<span class="by">- Orchard County Senior Services</span>
    <svg class="tail" style="left:48px" viewBox="0 0 24 14"><path d="M0 0L12 13L24 0" fill="#fff" stroke="#555" stroke-width="2"/></svg></div>
  <div class="abs qmark" style="left:318px;top:2866px">“</div>

  <div class="abs quote" style="left:611px;top:2880px;width:268px;height:233px;padding:40px 22px 0 24px">“Reed is easy to work with and his expertise allows you to tailor your training to the specific needs of your agency. We highly recommend Reed and his company.”<span class="by">- Community Action Partnership<br>of North Ridgeland</span>
    <svg class="tail" style="left:36px" viewBox="0 0 24 14"><path d="M0 0L12 13L24 0" fill="#fff" stroke="#555" stroke-width="2"/></svg></div>
  <div class="abs qmark" style="left:605px;top:2866px">“</div>

  <div class="abs quote" style="left:611px;top:3149px;width:268px;height:105px;padding:36px 22px 0 22px">“Reed saved our agency!”<span class="by" style="margin-top:4px">- Community Action For Uplift</span>
    <svg class="tail" style="left:36px" viewBox="0 0 24 14"><path d="M0 0L12 13L24 0" fill="#fff" stroke="#555" stroke-width="2"/></svg></div>
  <div class="abs qmark" style="left:605px;top:3135px">“</div>
</section>

<footer class="abs footer">
  <div class="abs logo" style="left:251px;top:37px;font-size:28px;color:var(--white)">
    <span class="mark" style="width:48px;height:48px;background:var(--white)"></span>TRBVEX LANE
  </div>
  <div class="addr">4180 LARKMOOR COURT<br>ALDER FALLS, GEORGIA 30099<br>(555) 014-2231</div>
  <div class="btn">CONTACT US</div>
  <ul class="links"><li>HOME</li><li>SERVICES</li><li>ROMA</li><li>MADD</li><li>RESOURCES</li><li>CONTACT</li></ul>
  <div class="copy">2022 © Trbvex Lane, LLC . All Rights Reserved</div>
  <div class="social"><span></span><span></span><span></span><span></span></div>
</footer>

</body>
</html>
```